依頼詳細
今回依頼するのは、500mlのビンの外箱です。

ビンの形状はワインボトルに似ています。

■依頼するビンの外箱のサイズは 高さ30cm×横7cm×奥行7cm の 細長い四角柱型。
■4面の中でデザイン箇所は、3面。1面は成分表示やお召し上がり方を記載します。
■ターゲットは20代~30代の女性向け
■商品の品質には絶対の自信があります。
■商品名は「ソフィレア」 Sofirea
■ダイエット効果や、美容、健康に重点を置いた商品なので、デザインイメージは「美しい女性」。

記載項目
特に無し。
希望イメージ
シンプル 複雑
単色 カラフル
暗い 明るい
日常 高級
遊び心 厳粛
未来的 伝統的
女性的 男性的
希望する色
ゴールド、グリーン、シルバーなど。単色でもOK。
納品ファイル
• 高解像度JPG (.jpg)
• イラストレーター形式 (.ai)
補足説明
ビンのイメージを追加します。

色は水色で、形状は画像のものとほぼ同じです。ご参考までに・・。
■ 選んだ理由

素晴らしいデザインで、社内の中でも満場一致です!

■ 提案者全員のお礼・コメント

皆様、本当にありがとうございました。

初めての依頼でしたので、お時間を頂きましたが、大満足でした。

また是非ご参加をお待ちしております。

```html
<!DOCTYPE html>
<html lang="ja">
<head>
<meta charset="utf-8">
<title>Sofirea – Bottle Box</title>
<link rel="stylesheet" href="https://fonts.googleapis.com/css2?family=Cormorant+Garamond:ital,wght@1,500&display=swap">
<style>
  :root {
    --ink: #000000;
    --paper: #ffffff;
  }
  html, body {
    margin: 0;
    padding: 0;
    overflow: hidden;
    background: var(--paper);
  }
  .box-net {
    position: relative;
    width: 682px;
    height: 1200px;
    background: var(--ink);
    overflow: hidden;
  }
  .top-flap {
    position: absolute;
    top: 0;
    width: 223px;
    height: 152px;
    background: var(--paper);
  }
  .top-flap--left { left: 0; }
  .top-flap--right { right: 0; }

  .lid-figure {
    position: absolute;
    left: 318px;
    top: 0;
    width: 46px;
    height: 146px;
    background: linear-gradient(180deg, var(--paper) 0%, rgba(255,255,255,0.85) 60%, rgba(255,255,255,0) 100%);
    border-radius: 0 0 23px 23px;
  }

  .woman-figure {
    position: absolute;
    left: 268px;
    top: 216px;
    width: 190px;
    height: 984px;
    background:
      radial-gradient(ellipse 60% 48% at 50% 42%, var(--paper) 0%, var(--paper) 55%, rgba(255,255,255,0) 100%);
  }

  .brand-name {
    position: absolute;
    margin: 0;
    font-family: "Cormorant Garamond", "Garamond", serif;
    font-style: italic;
    font-weight: 500;
    color: var(--paper);
    white-space: nowrap;
    line-height: 1;
    transform: translate(-50%, -50%);
    mix-blend-mode: difference;
  }
  .brand-name--lid   { left: 341px; top: 178px; font-size: 32px; }
  .brand-name--front { left: 345px; top: 432px; font-size: 74px; }
  .brand-name--left  { left: 118px; top: 592px; font-size: 72px; }
  .brand-name--right { left: 568px; top: 592px; font-size: 72px; }
</style>
</head>
<body>
  <main class="box-net">
    <div class="top-flap top-flap--left"></div>
    <div class="top-flap top-flap--right"></div>

    <div class="lid-figure" role="img" aria-label="Small white silhouette of an elegant woman on the lid"></div>
    <div class="woman-figure" role="img" aria-label="Tall white silhouette of a slender, beautiful woman in profile"></div>

    <p class="brand-name brand-name--lid">Sofirea</p>
    <p class="brand-name brand-name--front">Sofirea</p>
    <p class="brand-name brand-name--left">Sofirea</p>
    <p class="brand-name brand-name--right">Sofirea</p>
  </main>
</body>
</html>
```